Upscale business cards needed for family business

We need professional business cards created for several family members. We are a family business holding company. We would like these relatively simple and straightforward, but also with a unique element to set them apart. Probably stick with neutral and simple colors - white, grey etc. We need space for the traditional elements, including name, title, address, email/phone number. And we will be creating several from this template so it needs to be template that is easy to switch information in and out of.

Industry/Entity Type

Business

Contact Information for Business Card

Please include the attached Dunmore Ventures logo.

Requirements
Must have
• The attached Dunmore Ventures logo.

```html
<!DOCTYPE html>
<html lang="en">
<head>
<meta charset="utf-8">
<title>Dunmore Ventures – Business Card</title>
<link rel="stylesheet" href="https://fonts.googleapis.com/css2?family=Roboto:wght@400;500;700&display=swap">
<style>
  :root {
    --backdrop: #9b9b9b;
    --card: #ffffff;
    --band-grey: #707073;
    --band-edge: #55555a;
    --text-grey: #6a6a6d;
    --icon-grey: #5f5f62;
    --band-black: #0b0b0b;
    --accent-gold: #c9a233;
  }
  * { margin: 0; padding: 0; box-sizing: border-box; }
  html, body {
    width: 1105px; height: 1200px; overflow: hidden;
    background: var(--backdrop);
    font-family: "Roboto", Arial, sans-serif;
  }
  .canvas { position: relative; width: 1105px; height: 1200px; }

  .card {
    position: absolute; left: 182px; width: 746px; height: 425px;
    background: var(--card);
  }
  .card--front { top: 119px; }
  .card--back { top: 635px; }

  /* front */
  .brand-tab {
    position: absolute; left: 0; top: 95px; width: 28px; height: 72px;
    background: var(--band-grey);
  }
  .brand-name {
    position: absolute; left: 40px; top: 95px; width: 320px; height: 72px;
    display: flex; align-items: center; justify-content: center;
    font-size: 27px; font-weight: 500; color: var(--band-edge);
    letter-spacing: 0.5px;
  }
  .identity-band {
    position: absolute; left: 381px; top: 95px; width: 365px; height: 72px;
    background: var(--band-grey);
    border-left: 5px solid var(--band-edge);
    padding: 6px 0 0 19px; color: #fff;
  }
  .identity-band .person-name { font-size: 27px; font-weight: 500; line-height: 34px; }
  .identity-band .designation { font-size: 19px; font-weight: 700; line-height: 24px; }

  .contact-list {
    position: absolute; left: 407px; top: 196px; list-style: none;
    color: var(--text-grey); font-size: 19.5px; line-height: 25px;
  }
  .contact-list li { display: flex; align-items: flex-start; gap: 10px; }
  .contact-list li + li { margin-top: 7px; }
  .contact-list li.address { margin-bottom: 27px; }
  .contact-list svg { flex: none; width: 18px; height: 18px; margin-top: 4px; }

  /* back */
  .brand-strip {
    position: absolute; left: 0; top: 134px; width: 746px; height: 157px;
    background: var(--band-black);
    display: flex; align-items: center; justify-content: center;
  }
  .brand-strip .brand-mark {
    font-size: 32px; font-weight: 500; color: var(--accent-gold);
    letter-spacing: 1px;
  }
</style>
</head>
<body>
<main class="canvas">

  <section class="card card--front" aria-label="Business card front">
    <div class="brand-tab"></div>
    <div class="brand-name">Dunmore Ventures Inc.</div>

    <div class="identity-band">
      <p class="person-name">Person Name</p>
      <p class="designation">Designatiom</p>
    </div>

    <ul class="contact-list">
      <li class="address">
        <svg viewBox="0 0 18 18" aria-hidden="true"><circle cx="9" cy="9" r="9" fill="var(--icon-grey)"/><path d="M9 4 L13.5 9 H10.5 V13.5 H7.5 V9 H4.5 Z" fill="#fff"/></svg>
        <span>Consectetur adipiscing elit,<br>Donec accumsan.</span>
      </li>
      <li>
        <svg viewBox="0 0 18 18" aria-hidden="true"><circle cx="9" cy="9" r="9" fill="var(--icon-grey)"/><path d="M6 4.5 L7.8 4.5 L8.5 7 L7.3 8 Q8.3 10 10 10.7 L11 9.5 L13.5 10.2 L13.5 12 Q12.5 13.5 10.5 13 Q6 11.5 5 7 Q4.8 5.2 6 4.5 Z" fill="#fff"/></svg>
        <span>123 4564 7899</span>
      </li>
      <li>
        <svg viewBox="0 0 18 18" aria-hidden="true"><circle cx="9" cy="9" r="9" fill="var(--icon-grey)"/><rect x="6" y="4" width="6" height="3" fill="#fff"/><rect x="4" y="7.5" width="10" height="4.5" rx="1" fill="#fff"/><rect x="6" y="11" width="6" height="3" fill="#fff"/></svg>
        <span>123 4564 7899</span>
      </li>
      <li>
        <svg viewBox="0 0 18 18" aria-hidden="true"><circle cx="9" cy="9" r="9" fill="var(--icon-grey)"/><rect x="4.5" y="6" width="9" height="6.5" rx="1" fill="#fff"/><path d="M4.8 6.3 L9 9.6 L13.2 6.3" stroke="var(--icon-grey)" stroke-width="1" fill="none"/></svg>
        <span>name@dunmoreventures.com</span>
      </li>
      <li>
        <svg viewBox="0 0 18 18" aria-hidden="true"><circle cx="9" cy="9" r="9" fill="var(--icon-grey)"/><circle cx="9" cy="9" r="4.8" fill="none" stroke="#fff" stroke-width="1.3"/><path d="M4.2 9 H13.8 M9 4.2 Q6.5 9 9 13.8 M9 4.2 Q11.5 9 9 13.8" stroke="#fff" stroke-width="1" fill="none"/></svg>
        <span>www.dunmoreventures.com</span>
      </li>
    </ul>
  </section>

  <section class="card card--back" aria-label="Business card back">
    <div class="brand-strip">
      <span class="brand-mark">Dunmore Ventures Inc.</span>
    </div>
  </section>

</main>
</body>
</html>
```